Creative & Professional Business Card for hair salon

We are looking to update our business cards. Our salon is creative, modern, progressive and professional and looking for a design that will reflect this.

```html
<!DOCTYPE html>
<html lang="en">
<head>
<meta charset="utf-8">
<title>Minds in the Sky – Business Cards</title>
<link href="https://fonts.googleapis.com/css2?family=Open+Sans:wght@300;400&display=swap" rel="stylesheet">
<style>
  :root{
    --page:#ecebe8;
    --sky-deep:#5d88c2;
    --sky-mid:#8fb2dc;
    --sky-pale:#d9e6f3;
    --paper:#fbfbfc;
    --brand:#5f9aa8;
    --ink:#4d6a93;
    --ink-soft:#5f779b;
    --band:rgba(120,128,160,.55);
    --white:#ffffff;
  }
  *{box-sizing:border-box;margin:0;padding:0}
  html,body{width:1200px;height:942px;overflow:hidden}
  body{background:var(--page);font-family:"Open Sans",Arial,sans-serif;position:relative}

  .card{position:absolute;left:250px;width:700px;height:400px;overflow:hidden;
        box-shadow:0 6px 18px rgba(0,0,0,.18)}
  .card--front{top:46px}
  .card--back{top:496px}

  .sky{position:absolute;inset:0}
  .card--front .sky{
    background:
      radial-gradient(ellipse 45% 60% at 15% 85%, rgba(255,255,255,.85), transparent 70%),
      radial-gradient(ellipse 40% 45% at 55% 95%, rgba(255,255,255,.7), transparent 70%),
      radial-gradient(ellipse 60% 60% at 40% 10%, rgba(255,255,255,.55), transparent 70%),
      linear-gradient(160deg,var(--sky-pale) 0%,var(--sky-mid) 45%,var(--sky-deep) 100%);
  }
  .card--back .sky{
    background:
      radial-gradient(ellipse 50% 45% at 25% 95%, rgba(200,214,232,.9), transparent 70%),
      radial-gradient(ellipse 45% 40% at 75% 100%, rgba(190,206,228,.85), transparent 70%),
      linear-gradient(180deg,var(--paper) 0%,var(--paper) 45%,var(--sky-pale) 75%,#c4d4e8 100%);
  }

  .brand{position:absolute;display:flex;align-items:center;gap:12px;
         color:var(--brand);font-weight:300;font-size:26px;letter-spacing:.5px;white-space:nowrap}
  .brand__dot{width:12px;height:12px;border-radius:50%;background:var(--brand)}
  .card--front .brand{left:50px;top:56px}
  .card--back .brand{right:50px;top:56px}

  .contacts{position:absolute;left:360px;top:136px;list-style:none}
  .contacts li{display:flex;align-items:center;gap:14px;height:36px;
               color:var(--ink-soft);font-size:18px;letter-spacing:.3px;white-space:nowrap}
  .contacts svg{width:20px;height:20px;flex:none;fill:var(--ink)}

  .social-band{position:absolute;left:0;right:0;bottom:40px;height:44px;background:var(--band);
               display:flex;align-items:center;gap:14px;padding-left:50px;
               color:var(--white);font-size:19px;letter-spacing:.3px}
  .social-band__mark{width:18px;height:18px;background:var(--ink)}

  .appointment{position:absolute;left:50px;top:150px;width:340px}
  .appointment__label{color:var(--ink);font-size:17px;margin-bottom:28px}
  .appointment__line{height:1.5px;background:var(--ink-soft);margin-bottom:30px}
  .site{position:absolute;left:50px;bottom:70px;color:var(--ink);font-size:21px;letter-spacing:1.5px}
</style>
</head>
<body>

<section class="card card--front">
  <div class="sky" role="img" aria-label="Photograph of blue sky with soft white clouds"></div>
  <div class="brand"><span class="brand__dot"></span>Minds in the Sky by Tara Lenn</div>

  <ul class="contacts">
    <li><svg viewBox="0 0 24 24"><path d="M6.6 10.8a15 15 0 0 0 6.6 6.6l2.2-2.2c.3-.3.7-.4 1-.2 1.1.4 2.3.6 3.6.6.6 0 1 .4 1 1V20c0 .6-.4 1-1 1A17 17 0 0 1 3 4c0-.6.4-1 1-1h3.5c.6 0 1 .4 1 1 0 1.3.2 2.5.6 3.6.1.3 0 .7-.2 1z"/></svg>07 5000 1234</li>
    <li><svg viewBox="0 0 24 24"><path d="M2 5h20v14H2z M3.5 6.5 12 13l8.5-6.5" fill="none" stroke="#4d6a93" stroke-width="2"/></svg>salon@mindsinthesky.com.au</li>
    <li><svg viewBox="0 0 24 24"><g fill="none" stroke="#4d6a93" stroke-width="1.6"><circle cx="12" cy="12" r="9"/><ellipse cx="12" cy="12" rx="4" ry="9"/><path d="M3 12h18M5 7h14M5 17h14"/></g></svg>www.mindsinthesky.com.au</li>
    <li><svg viewBox="0 0 24 24"><path d="M12 2a7 7 0 0 0-7 7c0 5 7 13 7 13s7-8 7-13a7 7 0 0 0-7-7zm0 9.5A2.5 2.5 0 1 1 12 6.5a2.5 2.5 0 0 1 0 5z"/></svg>3/12 Harlow Street, Maple Bay</li>
  </ul>

  <div class="social-band"><span class="social-band__mark"></span>www.social.com/MindsInTheSkybyTaraLenn</div>
</section>

<section class="card card--back">
  <div class="sky" role="img" aria-label="Photograph of white clouds rising from the lower edge of a pale sky"></div>
  <div class="brand"><span class="brand__dot"></span>Minds in the Sky by Tara Lenn</div>

  <div class="appointment">
    <p class="appointment__label">Your Next Appointment</p>
    <div class="appointment__line"></div>
    <div class="appointment__line"></div>
  </div>

  <p class="site">www.mindsinthesky.com.au</p>
</section>

</body>
</html>
```